Modern Innovative Business Card Design

We require a nice, modern, clean business card design, ready for upload to Cardwello. Our company develops online banking software solutions for small financial insitutions. The design should be clean, professional, but yet not "corporate boring". See www.fintrola.com for an idea of business image and profile. The design should communicate innovation, be modern and fresh, yet look professional and established.

Target Market(s)

Finance industry, bankers, entrepreneurs

Industry/Entity Type

Financial

Contact Information for Business Card

Daniel Hargreave
CEO

FINTROLA BV
Lindenhofstraat 38
1072 KD Amsterdam
The Netherlands

Phone: +31 20 517 8063
Direct: +31 20 446 1975
Skype: daniel.fintrola
ceo@fintrola.com
www.fintrola.com

Font styles to use
Sans Serif

Requirements
Must have
• Should look clean, modern and professional. File should be ready for upload to cardwello.
Should not have
• Boring standard corporate layout

```html
<!DOCTYPE html>
<html lang="en">
<head>
<meta charset="utf-8">
<title>Fintrola – Business Card</title>
<link href="https://fonts.googleapis.com/css2?family=Didact+Gothic&display=swap" rel="stylesheet">
<style>
  :root {
    --backdrop: #7a4e20;
    --card: #ffffff;
    --lime: #95c643;
    --graphite: #505255;
    --rule: #6a6a6a;
  }
  * { margin: 0; padding: 0; box-sizing: border-box; }
  html, body {
    width: 1200px; height: 1000px; overflow: hidden;
    background: var(--backdrop);
    font-family: "Didact Gothic", "Century Gothic", sans-serif;
  }
  .card {
    position: absolute; left: 234px; top: 291px;
    width: 732px; height: 418px;
    background: var(--card);
    overflow: hidden;
  }
  .wave-block { position: absolute; left: 48px; top: 0; width: 246px; height: 90px; }
  .base-block {
    position: absolute; left: 48px; top: 226px;
    width: 246px; height: 192px; background: var(--lime);
  }
  .wordmark {
    position: absolute; left: 44px; top: 118px;
    font-size: 54px; letter-spacing: 2px; line-height: 1;
    color: var(--graphite);
  }
  .identity {
    position: absolute; right: 34px; top: 20px; text-align: right;
  }
  .identity .name {
    font-size: 36px; color: var(--lime); line-height: 1.1; letter-spacing: 0.5px;
  }
  .identity .role {
    font-size: 22px; color: var(--graphite); margin-top: 8px; letter-spacing: 1.5px;
  }
  .divider {
    position: absolute; left: 333px; right: 0; top: 226px;
    height: 1px; background: var(--rule);
  }
  .contact {
    position: absolute; right: 34px; top: 237px; text-align: right;
    font-size: 19.5px; line-height: 24.5px; color: var(--graphite);
  }
  .contact .web { color: var(--lime); }
</style>
</head>
<body>
  <div class="card">
    <svg class="wave-block" viewBox="0 0 246 90" aria-hidden="true">
      <path d="M0 0 H246 V60 C220 50 200 40 170 44 C120 52 80 86 40 84 C20 83 8 74 0 64 Z" fill="var(--lime)"/>
    </svg>
    <div class="wordmark">FINTROLA</div>
    <div class="base-block"></div>

    <div class="identity">
      <div class="name">Daniel Hargreave</div>
      <div class="role">CEO FINTROLA BV</div>
    </div>

    <div class="divider"></div>

    <div class="contact">
      <div>Lindenhofstraat 38</div>
      <div>1072 KD Amsterdam</div>
      <div>The Netherlands</div>
      <div>Phone: +31 20 517 8063</div>
      <div>Direct: +31 20 446 1975</div>
      <div>Skype: daniel.fintrola ceo@fintrola.com</div>
      <div class="web">www.fintrola.com</div>
    </div>
  </div>
</body>
</html>
```